Business card required for IT Consultancy Business - Tealbrook Consulting.
Company provides the whole nine yards of services across IT Architecture, design and execution.
Basically we provide consulting services to help businesses make sure their technology is enabling their business strategy.
Design for front and back required.
We would like the front of the card to inlcude:
Name
Title
Mobile number
email address
www.tbkc.com.au
Company logos attached.
Thank you
Industry/Entity Type
Business
Contact Information for Business Card
Name
Title
Mobile number
email address
www.tbkc.com.au
Look and feel
Each slider illustrates characteristics of the customer's brand and the style your logo design should communicate.

```html
<!DOCTYPE html>
<html lang="en">
<head>
<meta charset="utf-8">
<title>Tealbrook Consulting — Business Card</title>
<link href="https://fonts.googleapis.com/css2?family=Open+Sans:wght@400;600;700&display=swap" rel="stylesheet">
<style>
  :root{
    --backdrop:#3b332f;
    --card:#141516;
    --card-edge:#1d1e20;
    --blue:#2f80cc;
    --orange:#e8622c;
    --text:#e9e9e9;
    --muted:#6d6f73;
    --emboss:#3a3c40;
    --rule:#8c8e92;
  }
  *{box-sizing:border-box;margin:0;padding:0}
  html,body{width:1200px;height:864px;overflow:hidden}
  body{
    background:var(--backdrop);
    font-family:"Open Sans",Arial,sans-serif;
    display:flex;align-items:center;justify-content:center;gap:40px;
  }
  .card{
    width:540px;height:309px;
    background:linear-gradient(160deg,var(--card-edge),var(--card) 60%);
    border-radius:4px;
    position:relative;
    box-shadow:0 14px 30px rgba(0,0,0,.45);
    overflow:hidden;
  }
  /* back side */
  .card-back{display:flex;flex-direction:column;align-items:center;justify-content:center}
  .card-back .brand-name{
    font-weight:700;font-size:34px;color:var(--emboss);letter-spacing:.5px;
  }
  .card-back .website{
    margin-top:26px;font-size:14px;letter-spacing:7px;color:var(--muted);
  }
  /* front side */
  .card-front .brand{
    position:absolute;right:34px;top:88px;
    display:flex;align-items:center;gap:10px;
  }
  .card-front .brand-mark{width:16px;height:16px;border-radius:50%;background:var(--orange)}
  .card-front .brand-name{font-weight:700;font-size:26px;color:var(--blue);line-height:1}
  .contact{position:absolute;left:30px;top:142px;width:110px}
  .contact .person{font-weight:700;font-size:14px;line-height:20px;color:var(--blue);text-transform:uppercase;white-space:nowrap}
  .contact .role{
    font-size:14px;line-height:20px;color:var(--orange);text-transform:uppercase;
    padding-bottom:3px;border-bottom:1px solid var(--orange);width:100px;white-space:nowrap;
  }
  .contact ul{list-style:none;margin-top:8px}
  .contact li{display:flex;align-items:center;gap:10px;font-size:14px;color:var(--text);line-height:21px;white-space:nowrap}
  .contact svg{width:11px;height:11px;fill:var(--blue);flex:none}
  .rule{
    position:absolute;left:130px;right:34px;top:184px;height:1px;
    background:linear-gradient(90deg,#5a5c60,var(--rule));
  }
</style>
</head>
<body>
  <section class="card card-back">
    <div class="brand-name">Tealbrook Consulting</div>
    <div class="website">www.tbkc.com.au</div>
  </section>

  <section class="card card-front">
    <div class="brand">
      <span class="brand-mark"></span>
      <span class="brand-name">Tealbrook Consulting</span>
    </div>
    <div class="contact">
      <div class="person">Daniel Hargrove</div>
      <div class="role">CEO/Founder</div>
      <ul>
        <li><svg viewBox="0 0 12 12"><path d="M3 0h6a1 1 0 0 1 1 1v10a1 1 0 0 1-1 1H3a1 1 0 0 1-1-1V1a1 1 0 0 1 1-1zm0 2v7h6V2z"/></svg>0412 555 207</li>
        <li><svg viewBox="0 0 12 12"><path d="M0 2h12v8H0zm1 1v.4l5 3.2 5-3.2V3z"/></svg>daniel@tbkc.com.au</li>
        <li><svg viewBox="0 0 12 12"><circle cx="6" cy="6" r="6"/></svg>www.tbkc.com.au</li>
      </ul>
    </div>
    <div class="rule"></div>
  </section>
</body>
</html>
```